Redesign a TV Station website

Hello,
it looks like my explaination was not clear enough so i would like to clarify.
We are no longer designing a news website but rather a website for our TV station.
Please take a look at the current website we have .
http://www.vko.ci
We want a website similar to these two websites as example.

Please use the following websites as example
https://www.lumatel.com/
https://www.drw.com/

Here are my main menu on the horizontal bar
Accueil | Films | Series | Enfants | TV en Direct
P/S: You should disregard previous designs for the news website. We are designing purely a website for the TV stations. Please take a look at current site we have and design it similar to these two examples i mentioned
https://www.lumatel.com/
https://www.drw.com/
Updates

I needed more info for the project update.

Hello, We have updated design requirement for our project and hope it is much easier for you. You need to design the page based on the content on the link below: http://587opratv.com/template_obs.pdf You should use the same design as this to design the page http://587opratv.com/marc.jpeg The page will have same header style, color and design as the last link. However the content and layout of the page is the same as the first link. Please disregard the section that says "PAGE TYPE POUR MOBILE VERSION" Also disregard the title "MINI SITE LES ARPENTEURS "

Target Market(s)

TV Station

Number of Pages Required

1 page

Font styles to use
Sans Serif

Colors

Designer to choose colors to be used in the design.

Requirements
Must have
• N/A
Nice to have
• N/A
Should not have
• N/A

```html
<!DOCTYPE html>
<html lang="en">
<head>
<meta charset="utf-8">
<title>VKO – La Voix Kora Officielle</title>
<link href="https://fonts.googleapis.com/css2?family=Rubik:wght@300;400;500;700&display=swap" rel="stylesheet">
<style>
:root{
  --orange:#f26a10;
  --navy:#0c2f5e;
  --navy-deep:#082651;
  --navy-news:#123d73;
  --royal:#1d4fa0;
  --white:#ffffff;
  --muted:#cfd8e6;
  --ink:#3a3f4a;
  --footer:#1f1f1f;
  --footer-bar:#2b2b2b;
  --caption:#111111;
}
*{box-sizing:border-box;margin:0;padding:0}
html,body{width:1200px;height:2702px;overflow:hidden}
body{position:relative;font-family:'Rubik',sans-serif;background:var(--navy);color:var(--white)}
.abs{position:absolute}

.site-header{position:absolute;left:0;top:0;width:1200px;height:86px;background:var(--white)}
.brand{position:absolute;left:87px;top:14px;display:flex;align-items:center;gap:8px}
.brand-name{font-weight:700;font-size:46px;color:var(--navy);letter-spacing:1px;line-height:1}
.brand-dot{width:14px;height:14px;border-radius:50%;background:var(--orange)}
.main-nav{position:absolute;left:251px;top:34px;display:flex;font-size:14px;color:var(--ink)}
.main-nav span{padding:0 14px;border-right:1px solid var(--orange);line-height:16px}
.main-nav span:first-child{padding-left:0}
.main-nav span:last-child{border:none}
.live-btn{position:absolute;left:652px;top:24px}
.search{position:absolute;left:813px;top:25px;width:225px;height:36px;border:1px solid #c9ccd3;border-radius:18px;font-size:13px;color:#9aa0aa;padding:10px 0 0 50px}
.search svg{position:absolute;left:16px;top:10px}
.avatar{position:absolute;left:1062px;top:17px;width:52px;height:52px;border-radius:50%;background:radial-gradient(circle at 50% 40%,#e9825a,#8a5a7a 70%,#6b7a99)}

.hero{position:absolute;left:0;top:86px;width:1200px;height:514px;background:linear-gradient(100deg,#1a63b8 0%,#1b56a4 35%,#234c86 60%,#1a3a6e 100%)}
.hero-title{position:absolute;left:92px;top:307px;font-size:36px;font-weight:500;color:var(--orange);letter-spacing:.5px}
.hero-text{position:absolute;left:94px;top:370px;width:530px;font-size:12.5px;line-height:24px;color:var(--white)}
.hero-text em{font-style:normal;color:var(--orange)}
.btn{position:absolute;height:40px;border-radius:20px;font-size:14px;display:flex;align-items:center;justify-content:center;gap:28px}
.btn-programs{left:95px;top:509px;width:188px;background:var(--royal)}
.btn-watch{left:326px;top:509px;width:189px;background:var(--orange)}

.section-title{position:absolute;font-size:18px;font-weight:500;color:var(--orange)}
.section-sub{position:absolute;font-size:14px;color:var(--white)}
.see-all{position:absolute;font-size:15px;color:var(--orange);display:flex;align-items:center;gap:12px}
.arrow{position:absolute;width:54px;height:54px}

.trend-card{position:absolute;top:721px;width:231px;height:325px}
.trend-thumb{width:231px;height:263px}
.trend-caption{height:62px;background:var(--caption);display:flex;justify-content:space-between;align-items:center;padding:0 18px;font-size:13px}
.trend-caption b{font-weight:700}
.play{position:absolute;left:50%;top:50%;transform:translate(-50%,-50%)}

.show-card{position:absolute;top:1211px;width:326px}
.show-thumb{position:relative;width:326px;height:214px}
.show-meta{display:flex;justify-content:space-between;font-size:13px;margin-top:14px}
.show-date{font-size:12.5px;margin-top:12px}

.promo-banner{position:absolute;left:104px;top:1523px;width:992px;height:119px;background:linear-gradient(90deg,#1b3a7a,#3a3f8f 40%,#5c2e6e 70%,#2a4f9a)}

.news{position:absolute;left:0;top:1689px;width:1200px;height:514px;background:linear-gradient(90deg,#0f356a,#174a8a 50%,#1c5597)}
.news-card{position:absolute;top:1864px;width:257px}
.news-thumb{width:257px;height:171px}
.news-title{margin-top:22px;font-size:13px;font-weight:500;line-height:21px;text-transform:uppercase}
.news-meta{display:flex;justify-content:space-between;align-items:center;margin-top:8px;font-size:12.5px}
.news-meta span:last-child{color:var(--orange);font-size:10px;font-weight:500}

.signup{position:absolute;left:0;top:2203px;width:1200px;height:181px;background:var(--orange);text-align:center}
.signup h2{margin-top:36px;font-size:36px;font-weight:300}
.signup h2 b{font-weight:700}
.signup-btn{position:absolute;left:549px;top:103px;width:102px;height:36px;border-radius:18px;background:var(--royal);font-size:16px;line-height:36px}

.site-footer{position:absolute;left:0;top:2384px;width:1200px;height:267px;background:var(--footer)}
.footer-brand{position:absolute;left:0;width:1200px;top:50px;display:flex;justify-content:center;align-items:center;gap:8px}
.footer-brand .brand-name{color:var(--white)}
.social{position:absolute;width:34px;height:34px;border:2px solid var(--orange);border-radius:50%;top:146px}
.footer-nav{position:absolute;left:0;width:1200px;top:211px;display:flex;justify-content:center;font-size:12.5px;color:#e6e6e6}
.footer-nav span{padding:0 14px;border-right:1px solid #e6e6e6;line-height:14px}
.footer-nav span:last-child{border:none}
.footer-nav span:first-child{padding-right:28px}
.footer-bar{position:absolute;left:0;top:2651px;width:1200px;height:51px;background:var(--footer-bar);text-align:center;font-size:12.5px;line-height:51px;color:#e6e6e6}
</style>
</head>
<body>

<header class="site-header">
  <div class="brand"><span class="brand-name">VKO</span><span class="brand-dot"></span></div>
  <nav class="main-nav"><span>Accueil</span><span>Films</span><span>Series</span><span>Enfants</span><span>TV en Direct</span></nav>
  <svg class="live-btn" width="40" height="40" viewBox="0 0 40 40"><circle cx="20" cy="20" r="17" fill="none" stroke="var(--orange)" stroke-width="3"/><path d="M16 13 L27 20 L16 27Z" fill="var(--orange)"/></svg>
  <div class="search"><svg width="18" height="18" viewBox="0 0 18 18"><circle cx="7.5" cy="7.5" r="6" fill="none" stroke="#8a909a" stroke-width="1.5"/><path d="M12 12 L17 17" stroke="#8a909a" stroke-width="1.5"/></svg>Search vko</div>
  <div class="avatar" role="img" aria-label="User profile picture"></div>
</header>

<section class="hero" role="img" aria-label="Host presenting on the studio set"></section>
<h1 class="hero-title">VKO LAUNCH CEREMONY</h1>
<p class="hero-text">Relive in pictures the official launch party of <em>LA VOIX KORA OFFICIELLE</em> which was held on <em>Thursday December 19, 2019</em> in the Festival Hall of Hôtel Lagune Royale, in the presence of the Minister of Culture and many personalities from around the world media and culture</p>
<div class="btn btn-programs">Our Programs</div>
<div class="btn btn-watch">Watch video <svg width="26" height="26" viewBox="0 0 26 26"><circle cx="13" cy="13" r="11" fill="none" stroke="#fff" stroke-width="2"/><path d="M10.5 8 L17.5 13 L10.5 18Z" fill="#fff"/></svg></div>
<svg class="abs" style="left:1024px;top:516px" width="28" height="28" viewBox="0 0 28 28"><circle cx="14" cy="14" r="12" fill="none" stroke="#9fb0c8" stroke-width="1.5"/><path d="M16 9 L11 14 L16 19" fill="none" stroke="#9fb0c8" stroke-width="1.5"/></svg>
<svg class="abs" style="left:1069px;top:516px" width="28" height="28" viewBox="0 0 28 28"><circle cx="14" cy="14" r="12" fill="none" stroke="#fff" stroke-width="1.5"/><path d="M12 9 L17 14 L12 19" fill="none" stroke="#fff" stroke-width="1.5"/></svg>

<h2 class="section-title" style="left:94px;top:638px">TRANDING NOW</h2>
<p class="section-sub" style="left:94px;top:672px">Lorem Ipsum dolotr sit amit desoram</p>
<div class="see-all" style="left:1013px;top:663px">SEE ALL <svg width="14" height="14" viewBox="0 0 14 14"><circle cx="7" cy="7" r="6" fill="none" stroke="#fff" stroke-width="1.2"/><path d="M6 4.5 L8.5 7 L6 9.5" fill="none" stroke="#fff" stroke-width="1.2"/></svg></div>

<div class="trend-card" style="left:95px"><div class="trend-thumb" role="img" aria-label="Concert performer on stage" style="background:linear-gradient(160deg,#3a2a5e,#6a3f7a 50%,#2b2540)"></div><div class="trend-caption"><b>CONSERT 1</b><span>EP2</span></div></div>
<div class="trend-card" style="left:355px"><div class="trend-thumb" role="img" aria-label="Artist in music video" style="background:linear-gradient(160deg,#d9b7a8,#b88f7f 50%,#4a3a36)"></div><div class="trend-caption"><b>CONSERT 1</b><span>EP2</span></div></div>
<div class="trend-card" style="left:614px"><div class="trend-thumb" role="img" aria-label="Concert performer on stage" style="background:linear-gradient(160deg,#3a2a5e,#6a3f7a 50%,#2b2540)"></div><div class="trend-caption"><b>CONSERT 1</b><span>EP2</span></div></div>
<div class="trend-card" style="left:873px"><div class="trend-thumb" role="img" aria-label="News presenter in studio" style="background:linear-gradient(160deg,#2f7fd6,#5a6f9a 50%,#1d2a44)"></div><div class="trend-caption"><b>CONSERT 1</b><span>EP2</span></div></div>
<svg class="abs" style="left:192px;top:828px" width="46" height="46" viewBox="0 0 46 46"><circle cx="23" cy="23" r="20" fill="none" stroke="var(--orange)" stroke-width="4"/><path d="M19 15 L30 23 L19 31Z" fill="var(--orange)"/></svg>
<svg class="abs" style="left:447px;top:828px" width="46" height="46" viewBox="0 0 46 46"><circle cx="23" cy="23" r="20" fill="none" stroke="var(--orange)" stroke-width="4"/><path d="M19 15 L30 23 L19 31Z" fill="var(--orange)"/></svg>
<svg class="abs" style="left:706px;top:828px" width="46" height="46" viewBox="0 0 46 46"><circle cx="23" cy="23" r="20" fill="none" stroke="var(--orange)" stroke-width="4"/><path d="M19 15 L30 23 L19 31Z" fill="var(--orange)"/></svg>
<svg class="abs" style="left:966px;top:828px" width="46" height="46" viewBox="0 0 46 46"><circle cx="23" cy="23" r="20" fill="none" stroke="var(--orange)" stroke-width="4"/><path d="M19 15 L30 23 L19 31Z" fill="var(--orange)"/></svg>
<svg class="arrow" style="left:68px;top:834px" viewBox="0 0 54 54"><circle cx="27" cy="27" r="25" fill="none" stroke="#fff" stroke-width="2.5"/><path d="M31 18 L22 27 L31 36" fill="none" stroke="#fff" stroke-width="2.5"/></svg>
<svg class="arrow" style="left:1068px;top:834px" viewBox="0 0 54 54"><circle cx="27" cy="27" r="25" fill="none" stroke="#fff" stroke-width="2.5"/><path d="M23 18 L32 27 L23 36" fill="none" stroke="#fff" stroke-width="2.5"/></svg>

<h2 class="section-title" style="left:99px;top:1128px">LATEST SHOWS</h2>
<p class="section-sub" style="left:99px;top:1162px">Lorem Ipsum dolotr sit amit desoram</p>
<div class="see-all" style="left:1019px;top:1153px">SEE ALL <svg width="14" height="14" viewBox="0 0 14 14"><circle cx="7" cy="7" r="6" fill="none" stroke="#fff" stroke-width="1.2"/><path d="M6 4.5 L8.5 7 L6 9.5" fill="none" stroke="#fff" stroke-width="1.2"/></svg></div>

<div class="show-card" style="left:95px"><div class="show-thumb" role="img" aria-label="Talk show host promotional artwork" style="background:linear-gradient(120deg,#c8101a,#e3262e 60%,#f0b0a0)"><svg class="play" width="52" height="52" viewBox="0 0 52 52"><circle cx="26" cy="26" r="22" fill="none" stroke="var(--orange)" stroke-width="4"/><path d="M21 17 L34 26 L21 35Z" fill="var(--orange)"/></svg></div><div class="show-meta"><span>KORA TALKS</span><span>SE01 EP02</span></div><div class="show-date">DEC 29, 2019</div></div>
<div class="show-card" style="left:436px"><div class="show-thumb" role="img" aria-label="Artist in music video" style="background:linear-gradient(160deg,#dcbcad,#b88f7f 50%,#3a2e2a)"><svg class="play" width="52" height="52" viewBox="0 0 52 52"><circle cx="26" cy="26" r="22" fill="none" stroke="var(--orange)" stroke-width="4"/><path d="M21 17 L34 26 L21 35Z" fill="var(--orange)"/></svg></div><div class="show-meta"><span>KORA TALKS</span><span>SE01 EP02</span></div><div class="show-date">DEC 29, 2019</div></div>
<div class="show-card" style="left:776px"><div class="show-thumb" role="img" aria-label="Talk show host promotional artwork" style="background:linear-gradient(120deg,#c8101a,#e3262e 60%,#f0b0a0)"><svg class="play" width="52" height="52" viewBox="0 0 52 52"><circle cx="26" cy="26" r="22" fill="none" stroke="var(--orange)" stroke-width="4"/><path d="M21 17 L34 26 L21 35Z" fill="var(--orange)"/></svg></div><div class="show-meta"><span>KORA TALKS</span><span>SE01 EP02</span></div><div class="show-date">DEC 29, 2019</div></div>
<svg class="arrow" style="left:68px;top:1289px" viewBox="0 0 54 54"><circle cx="27" cy="27" r="25" fill="none" stroke="#fff" stroke-width="2.5"/><path d="M31 18 L22 27 L31 36" fill="none" stroke="#fff" stroke-width="2.5"/></svg>
<svg class="arrow" style="left:1068px;top:1289px" viewBox="0 0 54 54"><circle cx="27" cy="27" r="25" fill="none" stroke="#fff" stroke-width="2.5"/><path d="M23 18 L32 27 L23 36" fill="none" stroke="#fff" stroke-width="2.5"/></svg>

<div class="promo-banner" role="img" aria-label="Channel programme promotional banner with presenters and channel numbers"></div>

<section class="news" role="img" aria-label="Faint studio backdrop"></section>
<h2 class="section-title" style="left:94px;top:1744px">OUR NEWS</h2>
<p class="section-sub" style="left:94px;top:1778px">Lorem Ipsum dolotr sit amit desoram</p>
<div class="see-all" style="left:1013px;top:1769px">SEE ALL <svg width="14" height="14" viewBox="0 0 14 14"><circle cx="7" cy="7" r="6" fill="none" stroke="#fff" stroke-width="1.2"/><path d="M6 4.5 L8.5 7 L6 9.5" fill="none" stroke="#fff" stroke-width="1.2"/></svg></div>

<article class="news-card" style="left:189px"><div class="news-thumb" role="img" aria-label="Guests at the launch gala hall" style="background:linear-gradient(180deg,#2a3560,#4a5a8a 50%,#d8d8e0)"></div><h3 class="news-title">Media: official launch of the new Ivorian channel</h3><div class="news-meta"><span>12-29-2019</span><span>READ MORE</span></div></article>
<article class="news-card" style="left:472px"><div class="news-thumb" role="img" aria-label="City skyline at night" style="background:linear-gradient(180deg,#0a1a3a,#1a2f5a 60%,#c9a040)"></div><h3 class="news-title">Media: official launch of the new Ivorian channel</h3><div class="news-meta"><span>12-29-2019</span><span>READ MORE</span></div></article>
<article class="news-card" style="left:755px"><div class="news-thumb" role="img" aria-label="Partnership signing ceremony" style="background:linear-gradient(160deg,#e6e6ea,#9a86b0 50%,#5a4a6a)"></div><h3 class="news-title">Media: official launch of the new Ivorian channel</h3><div class="news-meta"><span>12-29-2019</span><span>READ MORE</span></div></article>
<svg class="arrow" style="left:68px;top:1919px" viewBox="0 0 54 54"><circle cx="27" cy="27" r="25" fill="none" stroke="#fff" stroke-width="2.5"/><path d="M31 18 L22 27 L31 36" fill="none" stroke="#fff" stroke-width="2.5"/></svg>
<svg class="arrow" style="left:1068px;top:1919px" viewBox="0 0 54 54"><circle cx="27" cy="27" r="25" fill="none" stroke="#fff" stroke-width="2.5"/><path d="M23 18 L32 27 L23 36" fill="none" stroke="#fff" stroke-width="2.5"/></svg>

<section class="signup">
  <h2>Receive the <b>latest updates</b> from the <b>VKO</b></h2>
  <div class="signup-btn">Sign Up</div>
</section>

<footer class="site-footer">
  <div class="footer-brand"><span class="brand-name">VKO</span><span class="brand-dot"></span></div>
  <span class="social" style="left:523px" aria-label="Social network"></span>
  <span class="social" style="left:582px" aria-label="Social network"></span>
  <span class="social" style="left:643px" aria-label="Social network"></span>
  <nav class="footer-nav"><span>Home</span><span>About</span><span>Services</span><span>Resources</span><span>Events</span><span>Blog</span><span>contact Us</span></nav>
</footer>
<div class="footer-bar">08 BP 412 Abidjan 08 | Plateau rue des Palmiers</div>

</body>
</html>
```